Sharper Daily Habits Qorafone App

I am looking to create an Qorafone app (support Qorafone 5 and above) that will inspire and empower the app user to be more productive through a creative, interative and simplistic user experience that teaches the 10 topics related to "Sharper Daily Habits". Please see attached zip files for the 10 topic as PDF files and 20 posters (20 jpg files) which include a quote related to the content bundle’s topic.

Target Market(s)

working professionals who desire to be more productive in their ways of doing

Industry/Entity Type

It Support

Font styles to use
Sans Serif

Colors
33a6d7
0255a3
9bcb3b
cadf82
33b8a4

Requirements
Must have
• don't really wanna say "ebook" style app which would be below my expectation, i expect something more creative than an "ebook" app. i prefer you use your creativity to come up with the design but if you are a bit lost, please read below.
• some specs in my mind:
• - 10 flash cards design for each of the topic so they can be used in a carousel style menu (see sample app screenshot 1 - 1st screen to the left)
• - when presenting a topic, the background should be the same as the flash card of the topic (see sample app screenshot 2 - the right most screen)
• - at the bottom of the topic screen, a audio play/pause buttons bar should be presented as the app will play audible version for the article.
• - the fashion of the sample app screen shots shouldn't be followed as it is an ancient fashion reflecting the content. I expect the fashion of the app should be modern and reflect the topic "sharper daily habits"
• Screens required:
• - Main menu screen: carosoul style presenting the 10 topics using flash cards, should have a "play/pause" button to play the audible topic
• - Topic screen: presents the text content of the topic with flash card design as the background, paging buttons when content spans over one page, have media player bar at bottom to "play/pause/fast forward/reverse" audible
Nice to have
• i have 20 posters with quotes that inspires the user. i would like to see the posters to be presented full screen with a "inspire me" button somewhere which will randomly display a poster to the user.

```html
<!DOCTYPE html>
<html lang="en">
<head>
<meta charset="utf-8">
<title>Sharper Daily Habits – Topic 3/20</title>
<link rel="stylesheet" href="https://fonts.googleapis.com/css2?family=Raleway:wght@300;400;500;600&display=swap">
<style>
  :root {
    --bg: #ffffff;
    --ink-dark: #5a4838;
    --ink-nav: #6e5f52;
    --ink-body: #9c9c9c;
    --ink-status: #4a4a4a;
    --track: #ececec;
    --knob: #e4e2e2;
    --cta-start: #f8c433;
    --cta-end: #f5992b;
    --cta-text: #ffffff;
  }
  * { box-sizing: border-box; margin: 0; padding: 0; }
  html, body {
    width: 737px; height: 1200px; overflow: hidden;
    background: var(--bg);
    font-family: "Raleway", "Helvetica Neue", Arial, sans-serif;
  }
  .screen { position: relative; width: 737px; height: 1200px; background: var(--bg); }

  .status-bar {
    position: absolute; top: 7px; left: 24px; right: 24px; height: 30px;
    display: flex; align-items: center; justify-content: space-between;
    font-size: 21px; font-weight: 500; color: var(--ink-status);
  }
  .status-left, .status-right { display: flex; align-items: center; gap: 8px; }
  .status-time { position: absolute; left: 50%; transform: translateX(-50%); }

  .nav-bar {
    position: absolute; top: 51px; left: 40px; right: 48px; height: 50px;
    display: flex; align-items: center; justify-content: space-between;
    color: var(--ink-nav); font-size: 26px; font-weight: 500;
  }
  .nav-back { display: flex; align-items: center; gap: 12px; }
  .nav-count {
    position: absolute; left: 50%; transform: translateX(-50%);
    font-size: 29px; font-weight: 600; color: var(--ink-dark);
  }

  .topic-hero {
    position: absolute; top: 128px; left: 0; width: 737px; height: 286px;
    background:
      radial-gradient(ellipse at 50% 70%, #c9c5c0 0%, transparent 55%),
      linear-gradient(180deg, #f1f1f1 0%, #e6e6e6 55%, #dcdcdc 100%);
  }

  .topic-title {
    position: absolute; top: 456px; left: 75px;
    font-size: 29px; font-weight: 600; color: var(--ink-dark); letter-spacing: -0.2px;
  }

  .topic-body {
    position: absolute; top: 538px; left: 76px; width: 580px;
    font-size: 20.5px; font-weight: 300; line-height: 26px; color: var(--ink-body);
    white-space: nowrap;
  }
  .topic-body p + p { margin-top: 50px; }
  .topic-body p.tight { margin-top: 24px; }

  .scroll-track {
    position: absolute; left: 679px; top: 524px; width: 2px; height: 584px;
    background: var(--track);
  }
  .scroll-knob {
    position: absolute; left: 666px; top: 576px; width: 28px; height: 28px;
    border-radius: 50%; background: var(--knob);
  }

  .play-audio {
    position: absolute; top: 1036px; left: 82px; width: 243px; height: 59px;
    border-radius: 30px;
    background: linear-gradient(90deg, var(--cta-start), var(--cta-end));
    display: flex; align-items: center; gap: 14px; padding-left: 9px;
    color: var(--cta-text); font-size: 18px; font-weight: 500; letter-spacing: 0.1px;
  }
</style>
</head>
<body>
<main class="screen">
  <div class="status-bar">
    <div class="status-left">
      <svg width="54" height="12" viewBox="0 0 54 12" aria-hidden="true">
        <circle cx="6" cy="6" r="5" fill="#4a4a4a"/>
        <circle cx="17" cy="6" r="5" fill="#4a4a4a"/>
        <circle cx="28" cy="6" r="5" fill="#4a4a4a"/>
        <circle cx="39" cy="6" r="4.3" fill="none" stroke="#4a4a4a" stroke-width="1.2"/>
        <circle cx="50" cy="6" r="4.3" fill="none" stroke="#4a4a4a" stroke-width="1.2"/>
      </svg>
      <span>KESTREL</span>
      <svg width="22" height="16" viewBox="0 0 22 16" aria-hidden="true">
        <path d="M1 5a14 14 0 0 1 20 0" fill="none" stroke="#4a4a4a" stroke-width="2.2"/>
        <path d="M5 9a8.5 8.5 0 0 1 12 0" fill="none" stroke="#4a4a4a" stroke-width="2.2"/>
        <circle cx="11" cy="13" r="2.3" fill="#4a4a4a"/>
      </svg>
    </div>
    <span class="status-time">4:21 PM</span>
    <div class="status-right">
      <svg width="12" height="20" viewBox="0 0 12 20" aria-hidden="true">
        <path d="M1 5l10 9-5 4V2l5 4L1 15" fill="none" stroke="#8a8a8a" stroke-width="1.5"/>
      </svg>
      <span>100%</span>
      <svg width="46" height="18" viewBox="0 0 46 18" aria-hidden="true">
        <rect x="0.75" y="0.75" width="40" height="16.5" rx="3" fill="none" stroke="#4a4a4a" stroke-width="1.5"/>
        <rect x="3" y="3" width="35.5" height="12" rx="1.5" fill="#6b5e54"/>
        <rect x="42.5" y="6" width="2.5" height="6" rx="1" fill="#4a4a4a"/>
      </svg>
    </div>
  </div>

  <nav class="nav-bar">
    <span class="nav-back">
      <svg width="14" height="24" viewBox="0 0 14 24" aria-hidden="true">
        <path d="M12 2L3 12l9 10" fill="none" stroke="#6e5f52" stroke-width="3" stroke-linecap="round" stroke-linejoin="round"/>
      </svg>
      Back
    </span>
    <span class="nav-count">3/20</span>
    <span class="nav-share">Share</span>
  </nav>

  <div class="topic-hero" role="img" aria-label="Photo of three colleagues chatting at a white table in a bright office"></div>

  <h1 class="topic-title">Productivity is Happiness</h1>

  <article class="topic-body">
    <p>Whenever you finish an activity, clean up to reduce<br>the friction to starting it the next time. E.g. clean the<br>kitchen when you finish cooking, or set aside your<br>running gear for your run tomorrow morning.</p>
    <p>We all waste an inordinate amount of time checking<br>and responding to email. I've got a bad habit of<br>wasting more time than I should ensuring my emails<br>come across as well worded and polite.</p>
    <p class="tight">If everyone knows that we are responding with brief,<br>straight to the point answers, then (with any luck) no<br>one will take it personally.</p>
  </article>

  <div class="scroll-track" aria-hidden="true"></div>
  <div class="scroll-knob" aria-hidden="true"></div>

  <div class="play-audio">
    <svg width="42" height="42" viewBox="0 0 42 42" aria-hidden="true">
      <circle cx="21" cy="21" r="19" fill="none" stroke="#fff" stroke-width="1.6"/>
      <path d="M17 14l11 7-11 7z" fill="none" stroke="#fff" stroke-width="1.6" stroke-linejoin="round"/>
    </svg>
    PLAY AS AUDIO
  </div>
</main>
</body>
</html>
```